Flight school sign for building, banner, and bilboard

This sign is primarily for use on the side of our flight school building to draw attention for current and future flight school students. We offer airplane and helicopter flight training, ground school training and seminars, airplane and helicopter rentals, multi-engine training, and more. I would like a professional but exciting sign that can be used across a multitude of signage options such as banners, banner ads, billboard, and other mediums so that our sign is consistent and recognizable.

Contact Information for Business Card

The business card should match our company sign somewhat but not exactly. We want good and exciting imagery or wording and energizing/exciting colors.

```html
<!DOCTYPE html>
<html lang="en">
<head>
<meta charset="utf-8">
<title>Meridian Aviation – Flight School Sign</title>
<link href="https://fonts.googleapis.com/css2?family=Montserrat:wght@600;700;800&display=swap" rel="stylesheet">
<style>
  :root{
    --red:#d91f2d;
    --red-deep:#b8141f;
    --navy:#1f2452;
    --white:#ffffff;
    --page:#f2f2f2;
  }
  *{margin:0;padding:0;box-sizing:border-box}
  html,body{width:900px;height:1200px;overflow:hidden}
  body{
    background:var(--page);
    font-family:'Montserrat',Arial,sans-serif;
    display:flex;align-items:center;justify-content:center;
  }
  .sign{
    position:relative;width:820px;height:500px;
    background:var(--red);overflow:hidden;
    box-shadow:0 4px 14px rgba(0,0,0,.18);
  }
  .sign__backdrop{
    position:absolute;inset:0;
    background:
      radial-gradient(ellipse 60% 45% at 50% 40%, rgba(120,8,16,.35), transparent 70%),
      linear-gradient(180deg,var(--red) 0%,var(--red-deep) 55%,var(--red) 100%);
  }
  .brand{
    position:absolute;top:0;left:0;right:0;height:213px;
    display:flex;flex-direction:column;align-items:center;justify-content:flex-end;
    padding-bottom:22px;gap:18px;
  }
  .brand__dot{
    width:74px;height:74px;border-radius:50%;
    border:6px solid var(--white);
  }
  .brand__name{
    color:var(--white);font-weight:600;font-size:27px;letter-spacing:.5px;
  }
  .rule{position:absolute;height:5px;background:var(--navy);width:410px}
  .rule--top{top:208px;left:0}
  .rule--bottom{top:396px;right:0}
  .headline{
    position:absolute;top:213px;left:0;right:0;height:183px;
    background:var(--white);
    display:flex;flex-direction:column;align-items:center;justify-content:center;
  }
  .headline__title{
    color:var(--red);font-weight:800;font-size:56px;line-height:1;letter-spacing:.5px;
  }
  .headline__tagline{
    color:var(--navy);font-weight:700;font-size:30px;margin-top:10px;
  }
  .contacts{
    position:absolute;top:401px;left:0;right:0;bottom:0;
    display:grid;grid-template-columns:1fr 1fr 1fr;align-items:center;
    padding:0 50px;
  }
  .contact{
    display:flex;flex-direction:column;align-items:center;gap:10px;
    color:var(--white);font-weight:700;font-size:13px;
  }
  .contact__icon{
    width:33px;height:33px;border-radius:50%;background:var(--white);
    display:flex;align-items:center;justify-content:center;
  }
  .contact__icon svg{width:19px;height:19px}
</style>
</head>
<body>
  <main class="sign">
    <div class="sign__backdrop" role="img" aria-label="Faint red-toned photo of a propeller aircraft in the sky"></div>

    <header class="brand">
      <span class="brand__dot"></span>
      <span class="brand__name">MERIDIAN AVIATION</span>
    </header>

    <span class="rule rule--top"></span>

    <section class="headline">
      <h1 class="headline__title">MERIDIAN AVIATION</h1>
      <p class="headline__tagline">Small step today,Giant leap tomorrow</p>
    </section>

    <span class="rule rule--bottom"></span>

    <footer class="contacts">
      <div class="contact">
        <span class="contact__icon">
          <svg viewBox="0 0 24 24"><path fill="#1f2452" d="M6.6 10.8a15.1 15.1 0 0 0 6.6 6.6l2.2-2.2c.3-.3.7-.4 1-.2 1.1.4 2.3.6 3.6.6.6 0 1 .4 1 1V20c0 .6-.4 1-1 1A17 17 0 0 1 3 4c0-.6.4-1 1-1h3.5c.6 0 1 .4 1 1 0 1.3.2 2.5.6 3.6.1.3 0 .7-.2 1z"/></svg>
        </span>
        <span class="contact__text">(555) 318 0270</span>
      </div>
      <div class="contact">
        <span class="contact__icon">
          <svg viewBox="0 0 24 24"><rect x="3" y="5" width="18" height="14" rx="2" fill="#1f2452"/><path d="M4 7l8 6 8-6" fill="none" stroke="#fff" stroke-width="1.6"/></svg>
        </span>
        <span class="contact__text">info@meridianflight.com</span>
      </div>
      <div class="contact">
        <span class="contact__icon">
          <svg viewBox="0 0 24 24" fill="none" stroke="#1f2452" stroke-width="1.8"><circle cx="12" cy="12" r="9"/><ellipse cx="12" cy="12" rx="4" ry="9"/><path d="M3 12h18M5 7h14M5 17h14"/></svg>
        </span>
        <span class="contact__text">www.meridianflight.com</span>
      </div>
    </footer>
  </main>
</body>
</html>
```